Singapore Restaurant Menu Design

We need a menu designed for our new Singapore inspire restaurant located here in New Plymouth New Zealand. More Information in attached documents.
Updates

Sick

Target Market(s)

New Zealanders

Colors

Designer to choose only greyscale colors for use in the design.

Requirements
Nice to have
• Images of Singapore food however we do not want this to distract from the overall menu design as we still want the menu to be super clean

```html
<!DOCTYPE html>
<html lang="en">
<head>
<meta charset="utf-8">
<title>Tanjong Singapore Cuisine – Menu</title>
<link href="https://fonts.googleapis.com/css2?family=Didact+Gothic&display=swap" rel="stylesheet">
<style>
  :root{
    --page-bg:#ffffff;
    --sheet:#f2f2f3;
    --ink:#222222;
    --ink-soft:#3a3a3a;
    --band:#f2d9c2;
    --fold:#333333;
    --photo-1:#8a6a44;
    --photo-2:#6f7d4a;
    --photo-3:#5a3322;
    --photo-4:#8a5a2e;
  }
  *{margin:0;padding:0;box-sizing:border-box}
  html,body{width:1200px;height:943px;overflow:hidden;background:var(--page-bg)}
  body{position:relative;font-family:"Didact Gothic",sans-serif;color:var(--ink)}
  .spread{position:absolute;left:83px;top:106px;width:1029px;height:732px;background:var(--sheet);box-shadow:4px 4px 8px rgba(0,0,0,.18)}
  .fold{position:absolute;left:598px;top:106px;width:1px;height:748px;background:var(--fold)}
  .brand{position:absolute;left:233px;top:150px;width:219px;text-align:center;font-size:34px;letter-spacing:6px;color:var(--ink)}
  .brand-mark{display:inline-block;width:10px;height:10px;background:var(--ink);margin-right:10px;vertical-align:middle}
  .brand-sub{position:absolute;left:233px;top:193px;width:219px;text-align:center;font-size:11px;letter-spacing:3px;color:var(--ink)}
  .menu-item{position:absolute;width:430px}
  .col-left{left:123px}
  .col-right{left:616px}
  .item-band{position:absolute;left:0;top:-2px;width:445px;height:22px;background:linear-gradient(90deg,var(--band) 0%,rgba(242,217,194,.55) 70%,rgba(242,217,194,0) 100%)}
  .item-title{position:relative;padding-left:13px;font-size:16px;line-height:18px;white-space:nowrap}
  .item-price{position:absolute;left:417px;top:0;font-size:16px;line-height:18px}
  .item-desc{position:relative;padding-left:13px;margin-top:5px;font-size:9.6px;line-height:18px;color:var(--ink-soft);width:420px}
  .photo-strip{position:absolute;left:83px;top:654px;width:1029px;height:184px;display:flex;gap:4px;-webkit-mask-image:linear-gradient(180deg,transparent 0%,#000 45%);mask-image:linear-gradient(180deg,transparent 0%,#000 45%)}
  .photo{height:100%}
  .photo-salad{width:192px;background:radial-gradient(circle at 45% 60%,#c98a3c,var(--photo-1) 70%)}
  .photo-rice{width:239px;background:radial-gradient(circle at 50% 40%,#eeeae0 0%,#c9c2a8 35%,var(--photo-2) 75%)}
  .photo-wings{width:290px;background:radial-gradient(ellipse at 50% 55%,#7a3a22,var(--photo-3) 60%,#6b5846 100%)}
  .photo-carrot-cake{flex:1;background:radial-gradient(ellipse at 45% 60%,#c08a4a 0%,var(--photo-4) 40%,#e8e6e0 70%)}
</style>
</head>
<body>
  <div class="spread"></div>

  <div class="brand"><span class="brand-mark"></span>TANJONG</div>
  <div class="brand-sub">SINGAPORE CUISINE</div>

  <!-- left page -->
  <div class="menu-item col-left" style="top:264px"><div class="item-band"></div><div class="item-title">Fried Wonton &nbsp;( 8 pieces )</div><div class="item-price">$10</div><div class="item-desc">Stuffed with choice of marinated spiced chicken / pork / pickled veggies with sweet soy dip</div></div>
  <div class="menu-item col-left" style="top:336px"><div class="item-band"></div><div class="item-title">GadoGado Salad V / *Vegan options available</div><div class="item-price">$12</div><div class="item-desc">A delicate salad of thinly sliced chinese cabbage, cucumber, beansprout, potatoes, french beans tossed in peanut dressing with boiled egg &amp; marinated prawns.</div></div>
  <div class="menu-item col-left" style="top:407px"><div class="item-band"></div><div class="item-title">Satay ( 6 sticks )</div><div class="item-price">$12</div><div class="item-desc">Grilled aromatic chicken / beef or tempeh (soy beans) on skewers accompanied by ketupat (rice cakes), cucumber, onions &amp; Singapore satay gravy</div></div>
  <div class="menu-item col-left" style="top:479px"><div class="item-band"></div><div class="item-title">BBQ Chicken Wings ( 5 pieces )</div><div class="item-price">$15</div><div class="item-desc">Singapore style soy marinated BBQ chicken wings made to order with sweet chili dip</div></div>
  <div class="menu-item col-left" style="top:533px"><div class="item-band"></div><div class="item-title">Fried Carrot Cake</div><div class="item-price">$10</div><div class="item-desc">Savoury steamed white radish cake stir-fry with prawns &amp; egg drizzled with sweet dark soy sauce</div></div>

  <!-- right page -->
  <div class="menu-item col-right" style="top:262px"><div class="item-band"></div><div class="item-title">Fried Wonton &nbsp;( 8 pieces )</div><div class="item-price">$10</div><div class="item-desc">Stuffed with choice of marinated spiced chicken / pork / pickled veggies with sweet soy dip</div></div>
  <div class="menu-item col-right" style="top:334px"><div class="item-band"></div><div class="item-title">GadoGado Salad V / *Vegan options available</div><div class="item-price">$12</div><div class="item-desc">A delicate salad of thinly sliced chinese cabbage, cucumber, beansprout, potatoes, french beans tossed in peanut dressing with boiled egg &amp; marinated prawns.</div></div>
  <div class="menu-item col-right" style="top:405px"><div class="item-band"></div><div class="item-title">Satay ( 6 sticks )</div><div class="item-price">$12</div><div class="item-desc">Grilled aromatic chicken / beef or tempeh (soy beans) on skewers accompanied by ketupat (rice cakes), cucumber, onions &amp; Singapore satay gravy</div></div>
  <div class="menu-item col-right" style="top:477px"><div class="item-band"></div><div class="item-title">BBQ Chicken Wings ( 5 pieces )</div><div class="item-price">$15</div><div class="item-desc">Singapore style soy marinated BBQ chicken wings made to order with sweet chili dip</div></div>
  <div class="menu-item col-right" style="top:531px"><div class="item-band"></div><div class="item-title">Fried Carrot Cake</div><div class="item-price">$10</div><div class="item-desc">Savoury steamed white radish cake stir-fry with prawns &amp; egg drizzled with sweet dark soy sauce</div></div>

  <div class="photo-strip">
    <div class="photo photo-salad" role="img" aria-label="Photo of a gado gado salad with egg, tofu and vegetables"></div>
    <div class="photo photo-rice" role="img" aria-label="Photo of coconut rice with boiled egg, anchovies and peanuts on a banana leaf"></div>
    <div class="photo photo-wings" role="img" aria-label="Photo of BBQ chicken wings on a white plate"></div>
    <div class="photo photo-carrot-cake" role="img" aria-label="Photo of fried carrot cake with dark soy sauce and beansprouts"></div>
  </div>

  <div class="fold"></div>
</body>
</html>
```